Business card - mobile service

O KiraTel is a mobile family safety service based on tablets and smartphones.
The business card must have:
BASIC INFO
Company Logo
Name
Position / Job Title: Co-founder
Mobile Phone Number: +55 (11) 5080 6172
Land Line: +55 (11) 9087 614352
Email Address: name@kiratel-example.com
Web Site URL: www.kiratel-example.com
PROMOTIONAL INFO
Try KiraTel free Today!
Your personal promo code: xxxx-2222-uuuu-7777-1234
Promo code text explanation with the instructions about the trial offer
Updates
Dears,
One more must have: the KiraTel slogan:
Industry/Entity Type
Safety
Look and feel
Each slider illustrates characteristics of the customer's brand and the style your logo design should communicate.

```html
<!DOCTYPE html>
<html lang="en">
<head>
<meta charset="utf-8">
<title>KiraTel business card</title>
<link href="https://fonts.googleapis.com/css2?family=Open+Sans:wght@400;700;800&display=swap" rel="stylesheet">
<style>
  :root {
    --page: #ffffff;
    --card-white: #ffffff;
    --card-yellow: #fcc918;
    --brand-blue: #0aa0dc;
    --ink: #1f1f1f;
    --shadow: rgba(0, 0, 0, 0.16);
  }
  * { box-sizing: border-box; margin: 0; padding: 0; }
  html, body {
    width: 1200px; height: 900px; overflow: hidden;
    background: var(--page);
    font-family: "Open Sans", Arial, sans-serif;
    color: var(--ink);
  }
  .canvas { position: relative; width: 1200px; height: 900px; }

  .card {
    position: absolute;
    width: 392px; height: 646px;
    border-radius: 38px;
    box-shadow: 12px 12px 6px var(--shadow);
    overflow: hidden;
  }
  .card--front { left: 142px; top: 119px; background: var(--card-white); }
  .card--back { left: 648px; top: 117px; background: var(--card-yellow); }

  /* Front: brand + promo */
  .brand {
    position: absolute; left: 0; right: 0; top: 298px;
    display: flex; justify-content: center; align-items: center; gap: 10px;
  }
  .brand__mark {
    width: 22px; height: 22px; border-radius: 50%;
    background: var(--brand-blue);
  }
  .brand__name {
    font-weight: 800; font-size: 60px; letter-spacing: -1px;
    color: var(--brand-blue); line-height: 1;
  }
  .slogan {
    position: absolute; left: 0; right: 0; top: 381px;
    text-align: center; font-size: 14.5px; line-height: 20px;
  }
  .promo {
    position: absolute; left: 0; right: 0; top: 435px;
    text-align: center; font-size: 16.5px; line-height: 24px;
  }
  .promo p + p { margin-top: 16px; }
  .promo p.promo__terms { margin-top: 23px; }

  /* Back: contact */
  .person { position: absolute; left: 36px; top: 405px; }
  .person__name { font-size: 23px; font-weight: 700; line-height: 30px; }
  .person__role { font-size: 16px; line-height: 26px; }
  .contacts { position: absolute; left: 36px; top: 478px; font-size: 16px; line-height: 24px; }
  .contacts dl { display: grid; grid-template-columns: auto auto; column-gap: 6px; }
  .contacts dt { font-weight: 700; }
  .contacts .online { margin-top: 23px; }
  .contacts .online dt { width: 16px; text-align: center; }
</style>
</head>
<body>
<main class="canvas">

  <section class="card card--front" aria-label="Card front">
    <div class="brand">
      <span class="brand__name">KiraTel</span>
      <span class="brand__mark"></span>
    </div>
    <p class="slogan">Your Family Safety Service</p>
    <div class="promo">
      <p>Try KiraTel free Today!</p>
      <p>Your personal promo code<br>xxxx-2222-uuuu-7777-1234</p>
      <p class="promo__terms">Promo code text explanation with<br>the instructions about the trial offer</p>
    </div>
  </section>

  <section class="card card--back" aria-label="Card back">
    <div class="person">
      <h1 class="person__name">Marta Lindqvist</h1>
      <p class="person__role">Co-founder</p>
    </div>
    <div class="contacts">
      <dl>
        <dt>Land Line</dt><dd>+55 (11) 9087 614352</dd>
        <dt>Mobile</dt><dd>+55 (11) 5080 6172</dd>
      </dl>
      <dl class="online">
        <dt>e</dt><dd>name@kiratel-example.com</dd>
        <dt>w</dt><dd>www.kiratel-example.com</dd>
      </dl>
    </div>
  </section>

</main>
</body>
</html>
```